Software Consulting Business Needs a Powerpoint Design

We need a powerpoint template design for a software consulting company called Marquil3, that we can use for a corporate overview presentation.

Our website/logo can be found at www.marquil3.com which should give you a good idea of our color scheme.

Here is a link to a zip file with the logos in AI format:

http://www.marquil3.com/logo/M3_Logo_Illustrator.zip

Here is a link to the Din font:

http://www.marquil3.com/logo/Din.zip

Sorry for delay. I was on vacation. A decision will be made by end of the week. Thanks!

```html
<!DOCTYPE html>
<html lang="en">
<head>
<meta charset="utf-8">
<title>Marquil3 — Presentation Title Slide</title>
<link rel="stylesheet" href="https://fonts.googleapis.com/css2?family=Open+Sans:wght@400;600&display=swap">
<style>
  :root {
    --navy: #2b3544;
    --accent: #e05a3f;
    --body-grey: #5a5a5a;
    --paper: #ffffff;
    --texture-grey: #e4e4e4;
  }
  * { margin: 0; padding: 0; box-sizing: border-box; }
  html, body {
    width: 1200px;
    height: 900px;
    overflow: hidden;
    background: var(--paper);
  }
  .slide {
    position: relative;
    width: 1200px;
    height: 900px;
    background: var(--paper);
    font-family: "Open Sans", Arial, sans-serif;
  }
  .texture-field {
    position: absolute;
    left: 447px;
    top: 0;
    width: 753px;
    height: 800px;
    background:
      radial-gradient(ellipse 520px 460px at 78% 34%, var(--texture-grey) 0%, rgba(228,228,228,0.55) 45%, rgba(255,255,255,0) 80%),
      linear-gradient(180deg, rgba(240,240,240,0.6) 0%, rgba(255,255,255,0) 85%);
  }
  .brand-band {
    position: absolute;
    left: 87px;
    top: 0;
    width: 360px;
    height: 900px;
    background: var(--navy);
  }
  .brand-mark {
    position: absolute;
    left: 0;
    top: 430px;
    width: 360px;
    display: flex;
    flex-direction: row;
    align-items: center;
    justify-content: center;
    gap: 16px;
  }
  .brand-square {
    width: 22px;
    height: 22px;
    background: var(--accent);
  }
  .brand-name {
    font-family: "Open Sans", Arial, sans-serif;
    font-weight: 600;
    font-size: 40px;
    color: var(--paper);
    line-height: 1;
  }
  .title-block {
    position: absolute;
    left: 505px;
    top: 432px;
  }
  .slide-title {
    font-weight: 400;
    font-size: 51px;
    letter-spacing: 0.3px;
    color: var(--accent);
    line-height: 1.2;
    white-space: nowrap;
  }
  .slide-subtext {
    margin-top: 16px;
    margin-left: 6px;
    font-weight: 600;
    font-size: 26px;
    line-height: 42px;
    color: var(--body-grey);
    white-space: nowrap;
  }
</style>
</head>
<body>
  <main class="slide">
    <div class="texture-field" role="img" aria-label="Soft grey halftone dot texture curving across the background"></div>

    <aside class="brand-band">
      <div class="brand-mark">
        <span class="brand-square" aria-hidden="true"></span>
        <span class="brand-name">Marquil3</span>
      </div>
    </aside>

    <section class="title-block">
      <h1 class="slide-title">PERSENTATION TITLE HERE</h1>
      <p class="slide-subtext">Sub Text here Sub Text here Sub Text here<br>Sub Text here Sub Text here Sub Text here<br>Sub Text here Sub Text here</p>
    </section>
  </main>
</body>
</html>
```